BEACON CABS

Taxi card design

Need changes very slow in replying to my messages.

Target Market(s)

Customers

Industry/Entity Type

Taxi

Contact Information for Business Card

See previous design

Font styles to use
Sans Serif

Colors
A7469A
B969AE
D3A5CF
EDDBEB
F8F0F9
6B429C
8869AF
B7A5CE
E3DAEB
F3F0F8

Requirements
Nice to have
• We are in the business of looking after people, not just driving vehicles front
Should not have
• Front number 01632 480 480 needs to big big

```html
<!DOCTYPE html>
<html lang="en">
<head>
<meta charset="utf-8">
<title>Beacon Cabs – Taxi Card</title>
<link rel="stylesheet" href="https://fonts.googleapis.com/css2?family=Roboto+Condensed:wght@400;700&display=swap">
<style>
  :root {
    --magenta: #A7469A;
    --violet: #6B429C;
    --violet-deep: #2E1F3F;
    --lilac: #EDDBEB;
    --lavender: #E3DAEB;
    --white: #FFFFFF;
    --amber-soft: #7A6235;
  }
  * { margin: 0; padding: 0; box-sizing: border-box; }
  html, body { width: 1200px; height: 686px; overflow: hidden; background: #ffffff; }
  body { font-family: "Roboto Condensed", Arial, sans-serif; color: var(--white); }

  .card { position: relative; width: 1200px; height: 686px; overflow: hidden;
    background: linear-gradient(100deg, var(--magenta) 0%, #8A4499 55%, var(--violet) 100%); }

  .hero { position: absolute; left: 0; top: 0; width: 1200px; height: 323px; }
  .hero-photo { position: absolute; left: 0; top: 0; width: 1200px; height: 299px;
    background: linear-gradient(100deg, #5B4A3A 0%, var(--amber-soft) 22%, var(--violet-deep) 50%, #6A5536 78%, #3E3346 100%); }

  .band { position: absolute; left: 0; width: 1200px; }
  .band.top { top: 0; height: 14px; background: var(--lavender); }
  .band.mid { top: 299px; height: 24px; background: var(--lilac); border-bottom: 4px solid var(--white); }

  .brand { position: absolute; left: 254px; top: 76px; }
  .brand-name { font-weight: 700; font-size: 78px; line-height: 1; letter-spacing: 1px; }
  .brand-est { position: absolute; left: 92px; top: 86px; font-size: 19px; font-weight: 400; white-space: nowrap; }
  .availability { position: absolute; left: 763px; top: 108px; font-size: 38px; font-weight: 700; }

  .services { position: absolute; left: 0; top: 214px; width: 1200px; display: flex;
    justify-content: center; align-items: center; gap: 52px;
    font-size: 35px; font-weight: 700; letter-spacing: .5px; }
  .services .star { width: 18px; height: 18px; }

  .contact { position: absolute; left: 0; top: 323px; width: 1200px; height: 363px; }
  .phone-main { position: absolute; left: 300px; top: 22px; display: flex; align-items: center; gap: 20px;
    font-size: 82px; font-weight: 700; }
  .phone-main .icon { width: 94px; height: 94px; }

  .phone-list { position: absolute; left: 30px; right: 30px; top: 148px; display: flex; justify-content: space-between; }
  .phone-item { display: flex; align-items: center; gap: 4px; font-size: 47px; font-weight: 700; }
  .phone-item .icon { width: 50px; height: 50px; }

  .details { position: absolute; left: 0; top: 236px; width: 1200px; display: flex; justify-content: center;
    align-items: center; font-size: 27px; font-weight: 400; }
  .details span { padding: 0 14px; }
  .details .divider { width: 2px; height: 40px; background: var(--white); padding: 0; }

  .address { position: absolute; left: 0; top: 308px; width: 1200px; text-align: center; font-size: 30px; font-weight: 400; }
</style>
</head>
<body>
<svg width="0" height="0" style="position:absolute">
  <defs>
    <symbol id="phone-bubble" viewBox="0 0 100 100">
      <path d="M50 6a42 42 0 1 0 22 78l20 8-6-18A42 42 0 0 0 50 6z" fill="none" stroke="#fff" stroke-width="7" stroke-linejoin="round"/>
      <path d="M36 27c3-2 6-1 7 2l4 8c1 3 0 5-2 6l-3 2c2 6 7 11 13 14l2-3c2-2 4-3 6-2l8 4c3 1 4 4 2 7l-3 4c-3 3-8 4-13 2-13-6-22-15-27-28-2-5-1-10 2-13z" fill="#fff"/>
    </symbol>
  </defs>
</svg>

<main class="card">
  <header class="hero">
    <div class="hero-photo" role="img" aria-label="Photograph of yellow taxis lined up on a city street"></div>
    <div class="band top"></div>
    <div class="brand">
      <span class="brand-name">BEACON CABS</span>
      <span class="brand-est">Established since 1986</span>
    </div>
    <div class="availability">24/7 Service</div>
    <nav class="services">
      <span>AIRPORT TRANSFERS</span>
      <svg class="star" viewBox="0 0 20 20"><path d="M10 1l2.6 6 6.4.5-4.9 4.2 1.5 6.3L10 14.6 4.4 18l1.5-6.3L1 7.5l6.4-.5z" fill="#fff"/></svg>
      <span>MINI BUSES</span>
      <svg class="star" viewBox="0 0 20 20"><path d="M10 1l2.6 6 6.4.5-4.9 4.2 1.5 6.3L10 14.6 4.4 18l1.5-6.3L1 7.5l6.4-.5z" fill="#fff"/></svg>
      <span>SCHOOL TRANSPORT</span>
    </nav>
    <div class="band mid"></div>
  </header>

  <section class="contact">
    <div class="phone-main">
      <svg class="icon"><use href="#phone-bubble"/></svg>
      <span>01632 480 480</span>
    </div>
    <div class="phone-list">
      <div class="phone-item"><svg class="icon"><use href="#phone-bubble"/></svg><span>01632 480 111</span></div>
      <div class="phone-item"><svg class="icon"><use href="#phone-bubble"/></svg><span>01632 480 222</span></div>
      <div class="phone-item"><svg class="icon"><use href="#phone-bubble"/></svg><span>01632 480 333</span></div>
    </div>
    <div class="details">
      <span>Freephone: 0808 157 0 246</span>
      <span class="divider"></span>
      <span>Email: ride@beaconcabs.co.uk</span>
      <span class="divider"></span>
      <span>Website: www.beaconcabs.co.uk</span>
    </div>
    <p class="address">Unit 4 Mill Yard, Harbour Lane, Eastbrook EB4 7QT</p>
  </section>
</main>
</body>
</html>
```